KLM Electric new logo and business card design

please view website to get information,
www.klmelectric-demo.com.au
also attached current business card.
open to all designs,
moving to new factory so this will start the launch of face-lift to company, will lead to other works,
Would like to keep Logo design but could do with a face lift?
on rear of card should mention Key products,
*transportable building
*light and heavy steel fabrication
*powdercoating
*all types of labels, name plates, wire and cable identification
*low and medium voltage switchboards
as a minimum start, feel free to value add,

KLM Electric Pty Ltd
14-22 Penwillow drive
Kelbrook South Vic 3990
Mark Delane
Director
Phone;
Fax;
Mobile
Email;

```html
<!DOCTYPE html>
<html lang="en">
<head>
<meta charset="utf-8">
<title>KLM Electric – Business Card</title>
<link href="https://fonts.googleapis.com/css2?family=Arimo:wght@400;700&display=swap" rel="stylesheet">
<style>
  :root {
    --backdrop: #d9dadb;
    --card-light: #fbfbfb;
    --card-mid: #ececec;
    --lobe-light: #ffffff;
    --lobe-shade: #d4d4d4;
    --ink: #5e5e5e;
    --ink-soft: #7a7a7a;
    --band-dark: #8c8c8c;
    --band-light: #d8d8d8;
    --band-text: #ffffff;
    --brand-red: #c8202a;
  }
  * { box-sizing: border-box; margin: 0; padding: 0; }
  html, body {
    width: 1200px; height: 900px; overflow: hidden;
    background: var(--backdrop);
    font-family: "Arimo", Arial, sans-serif;
  }
  .canvas {
    position: relative; width: 1200px; height: 900px;
    display: flex; flex-direction: column; align-items: center; justify-content: center; gap: 40px;
  }
  .card {
    position: relative; width: 620px; height: 380px; overflow: hidden;
    background: linear-gradient(135deg, var(--card-light) 0%, var(--card-mid) 100%);
    box-shadow: 0 6px 18px rgba(0,0,0,.18);
  }
  .card__lobe { position: absolute; top: 0; height: 380px; width: 340px; }
  .card--front .card__lobe { left: 0; }
  .card--back .card__lobe { right: 0; }

  .brand {
    position: absolute; display: flex; flex-direction: column; align-items: center; gap: 14px;
    width: 260px;
  }
  .card--front .brand { left: 20px; top: 120px; }
  .card--back .brand { right: 10px; top: 120px; }
  .brand__dot { width: 54px; height: 54px; border-radius: 50%; background: var(--brand-red); }
  .brand__name {
    font-size: 20px; font-weight: 700; color: var(--ink); text-align: center; line-height: 1.2;
  }

  .person { position: absolute; right: 38px; top: 30px; text-align: right; }
  .person__name { font-size: 32px; font-weight: 700; color: var(--ink); }
  .person__title { font-size: 14px; letter-spacing: .5px; color: var(--ink-soft); margin-top: 2px; }

  .address {
    position: absolute; right: 38px; top: 150px; text-align: right;
    font-size: 15px; line-height: 1.45; color: var(--ink);
  }
  .contacts {
    position: absolute; right: 38px; bottom: 28px;
    display: grid; grid-template-columns: auto auto; column-gap: 10px; row-gap: 2px;
    font-size: 15px; color: var(--ink);
  }
  .contacts dt { font-weight: 700; text-align: left; }
  .contacts dd { text-align: right; }
  .contacts .email-label { margin-top: 12px; }
  .contacts .email { margin-top: 12px; }

  .products { position: absolute; left: 0; top: 38px; width: 330px; list-style: none; }
  .products li {
    display: flex; align-items: center;
    min-height: 58px; margin-bottom: 22px; padding: 6px 16px;
    background: linear-gradient(90deg, var(--band-dark) 0%, var(--band-light) 100%);
    color: var(--band-text); font-weight: 700; font-size: 16px; line-height: 1.2;
    text-transform: uppercase; text-shadow: 0 1px 2px rgba(0,0,0,.35);
  }
</style>
</head>
<body>
<main class="canvas">

  <section class="card card--front" aria-label="Business card front">
    <svg class="card__lobe" viewBox="0 0 340 380" aria-hidden="true">
      <defs>
        <linearGradient id="lobeFront" x1="0" y1="0" x2="1" y2="1">
          <stop offset="0" stop-color="var(--lobe-light)"/>
          <stop offset="1" stop-color="var(--lobe-shade)"/>
        </linearGradient>
      </defs>
      <path d="M0,0 H200 C290,50 330,190 305,290 C290,350 250,380 200,380 H0 Z" fill="url(#lobeFront)"/>
    </svg>
    <div class="brand">
      <span class="brand__dot"></span>
      <span class="brand__name">KLM Electric Pty Ltd</span>
    </div>
    <div class="person">
      <h1 class="person__name">Mark Delane</h1>
      <p class="person__title">DIRECTOR</p>
    </div>
    <address class="address">14-22 Penwillow drive<br>Kelbrook South Vic 3990</address>
    <dl class="contacts">
      <dt>P:</dt><dd>+61 (0)3 9000 4127</dd>
      <dt>F:</dt><dd>+61 (0)3 9000 4128</dd>
      <dt>M:</dt><dd>+61 (0)400 555 209</dd>
      <dt class="email-label">E:</dt><dd class="email">mark.delane@klmelectric-demo.com.au</dd>
    </dl>
  </section>

  <section class="card card--back" aria-label="Business card back">
    <svg class="card__lobe" viewBox="0 0 340 380" aria-hidden="true">
      <defs>
        <linearGradient id="lobeBack" x1="1" y1="0" x2="0" y2="1">
          <stop offset="0" stop-color="var(--lobe-light)"/>
          <stop offset="1" stop-color="var(--lobe-shade)"/>
        </linearGradient>
      </defs>
      <path d="M340,0 H140 C50,50 10,190 35,290 C50,350 90,380 140,380 H340 Z" fill="url(#lobeBack)"/>
    </svg>
    <ul class="products">
      <li>Transportable building</li>
      <li>Light and heavy steel fabrication powdercoating</li>
      <li>All types of labels, name plates, wire and cable identification</li>
      <li>Low and medium voltage switchboards</li>
    </ul>
    <div class="brand">
      <span class="brand__dot"></span>
      <span class="brand__name">KLM Electric Pty Ltd</span>
    </div>
  </section>

</main>
</body>
</html>
```